GPS Tracker Business Card Design

We need a business card for a GPS Vehicle tracking company. We sell the hardware for the vehicle and the software platform to monitor your vehicle/s. Including high asset non-powered vehicles like a trailer using our solar powered unit.
We like using dark blue to different shades of blue along with gold. We have phone apps for Android and Apple devices.

We have a platform for families wanting to track their teenage driver and children; Plus a Fleet vehicle tracking platform.

Features: unlimited number of vehicles and/or assets including snow mobiles forklifts generators trailers airport equipment

Reports for driving behavior reports and alerts dashboard fleet maintenace timeline view and replay geofence real time alerts logbook scheduling route optimization accounting integration fleet grouping closest vehicle locator On Board Diagnostics.

Benefits: Increased productivity improved fuel efficiency organizing your business improve time management simplify back end processes, reduce fleet fuel efficiency and expenses increase fleet security etc..

Please view website: Velmorix.com

Industry/Entity Type

Business

Contact Information for Business Card

Harold P Simkins

```html
<!DOCTYPE html>
<html lang="en">
<head>
<meta charset="UTF-8">
<title>Velmorix Business Card</title>
<link href="https://fonts.googleapis.com/css2?family=Arimo:wght@400;700&display=swap" rel="stylesheet">
<style>
  :root {
    --page-bg: #ecebe8;
    --navy: #0d1f4f;
    --navy-deep: #06143a;
    --steel: #3b6fa8;
    --brand-blue: #1f5fb4;
    --ink: #1c1c1c;
    --tag-grey: #8a8a8a;
    --rule: #2a3a6a;
    --card-white: #f7f7f6;
  }
  * { margin: 0; padding: 0; box-sizing: border-box; }
  html, body {
    width: 1200px; height: 902px; overflow: hidden;
    background: var(--page-bg);
    font-family: "Arimo", Arial, sans-serif;
  }
  .stage {
    position: relative; width: 1200px; height: 902px;
    display: flex; align-items: center; justify-content: center; gap: 40px;
  }
  .card {
    position: relative; width: 540px; height: 309px;
    box-shadow: 0 6px 18px rgba(0,0,0,0.18);
    overflow: hidden;
  }
  .card-back {
    background: linear-gradient(160deg, var(--navy) 0%, var(--navy-deep) 100%);
  }
  .card-back .scene-photo {
    position: absolute; inset: 0;
    background: radial-gradient(ellipse 60% 70% at 38% 45%, #7fa7d4 0%, #3b6fa8 35%, rgba(13,31,79,0) 100%);
  }
  .card-front {
    background: var(--card-white);
    border: 7px solid var(--navy);
  }
  .brand-block {
    position: absolute; left: 0; right: 0; top: 34px;
    display: flex; flex-direction: column; align-items: center;
  }
  .brand {
    font-size: 70px; font-weight: 400; letter-spacing: -1px;
    color: var(--ink); line-height: 1;
  }
  .brand-mark {
    display: inline-block; width: 9px; height: 9px; border-radius: 50%;
    background: var(--brand-blue); margin-left: 6px; vertical-align: top; margin-top: 4px;
  }
  .tagline {
    margin-top: 4px;
    font-size: 21px; color: var(--tag-grey); letter-spacing: 0.5px;
  }
  .rule {
    position: absolute; left: 40px; right: 40px; top: 142px;
    height: 1.5px; background: var(--rule);
  }
  .holder {
    position: absolute; left: 0; right: 0; top: 156px; text-align: center;
    font-size: 27px; font-weight: 700; color: var(--brand-blue);
  }
  .contact {
    position: absolute; left: 0; right: 0; top: 196px;
    text-align: center; list-style: none;
    font-size: 15px; line-height: 20px; color: var(--ink);
  }
</style>
</head>
<body>
  <main class="stage">
    <section class="card card-back">
      <div class="scene-photo" role="img" aria-label="Photo of hands typing on a laptop with a world map and connected location markers overlay"></div>
    </section>
    <section class="card card-front">
      <div class="brand-block">
        <div class="brand">Velmorix<span class="brand-mark"></span></div>
        <div class="tagline">Every Mile, Every Move</div>
      </div>
      <div class="rule"></div>
      <h1 class="holder">Harold P Simkins</h1>
      <ul class="contact">
        <li>866-555-0142</li>
        <li>www.velmorix.com</li>
        <li>harold@velmorix.com</li>
        <li>418 N. Harbor Lane, Suite 310 Alder Grove, CA 91612</li>
      </ul>
    </section>
  </main>
</body>
</html>
```